Hi,

I have just started up a business called VELUMO in Melbourne. We run fun street art tours around Melbourne's CBD.

I need to create a design for the back side of my business cards. I have designed the front side (simply with my logo) however, I am having trouble designing the reverse side in a professional manner. I have attached pictures of what I have done.

The picture attached titled "VELUMO Business Cards Back" has all the information that I require on the back side of my business cards; although displayed in an amateur and simple way. As displayed in the picture, I need: the VELUMO logo, the website URL, the booking details (phone - 0481 556 217 & email - bookings@velumo.com.au) and the service description ($20, One Hour, Tours Daily, Meet at Carrow Rd Terminal). I would also like to use the font in the picture supplied which is "source-sans-pro".

The VELUMO tours are for tourists and are relaxed, entertaining and fun! I would like the design to reflect this.

Target Market(s)

Backpackers & University Students

Industry/Entity Type

Business

Requirements
Must have
• The VELUMO logo, the website URL, the booking details (phone - 0481 556 217 & email - bookings@velumo.com.au) and the service description ($20, One Hour, Tours Daily, Meet at Carrow Rd Terminal).

```html
<!DOCTYPE html>
<html lang="en">
<head>
<meta charset="utf-8">
<title>VELUMO – Business Cards</title>
<link rel="stylesheet" href="https://fonts.googleapis.com/css2?family=Source+Sans+3:wght@400;600;700;900&family=Tinos:wght@700&display=swap">
<style>
  :root {
    --backdrop: #d6d6d6;
    --card-light: #ebe8e9;
    --ink: #0b0b0b;
    --wine: #8e1b1b;
    --coral: #f05a4b;
    --signal-red: #e8282a;
    --white: #ffffff;
  }
  * { margin: 0; padding: 0; box-sizing: border-box; }
  html, body {
    width: 1200px; height: 985px; overflow: hidden;
    background: var(--backdrop);
    font-family: "Source Sans 3", "Source Sans Pro", sans-serif;
  }
  .canvas { position: relative; width: 1200px; height: 985px; }
  .card {
    position: absolute; left: 220px; width: 760px; height: 434px;
    border-radius: 28px; overflow: hidden;
    background: var(--card-light);
    box-shadow: 0 10px 24px rgba(0,0,0,0.18);
  }
  .card--front { top: 36px; }
  .card--back { top: 515px; }
  .card__waves { position: absolute; inset: 0; width: 100%; height: 100%; }
  .wave--wine { fill: var(--wine); }
  .wave--coral { fill: var(--coral); }
  .wave--ink { fill: var(--ink); }

  .wordmark {
    position: absolute; left: 0; right: 0; top: 70px;
    display: flex; align-items: center; justify-content: center; gap: 18px;
  }
  .wordmark__dot {
    width: 34px; height: 34px; border-radius: 50%; background: var(--coral);
  }
  .wordmark__name {
    font-weight: 900; font-size: 92px; letter-spacing: 4px;
    color: var(--ink); line-height: 1;
  }

  .tagline {
    position: absolute; left: 150px; top: 240px;
    font-family: "Tinos", "Times New Roman", serif; font-weight: 700;
    font-size: 30px; line-height: 1.15; color: var(--white);
  }

  .contacts { position: absolute; left: 34px; top: 220px; list-style: none; }
  .contacts li {
    display: flex; align-items: center; gap: 16px;
    height: 38px; font-size: 22px; font-weight: 600; color: var(--white);
  }
  .contacts svg { width: 26px; height: 26px; flex: none; }

  .details { position: absolute; left: 418px; top: 292px; list-style: none; }
  .details li {
    position: relative; z-index: 2;
    display: flex; align-items: center; gap: 12px;
    height: 38px; font-size: 22px; font-weight: 600; color: var(--white);
  }
  .details svg { width: 22px; height: 22px; flex: none; }

  .price-badge { position: absolute; left: 600px; top: 248px; width: 110px; height: 150px; z-index: 1; }
  .price-badge__text {
    font-family: "Source Sans 3", sans-serif; font-weight: 700; font-size: 26px; fill: var(--white);
  }
</style>
</head>
<body>
<main class="canvas">

  <section class="card card--front" aria-label="Card front">
    <svg class="card__waves" viewBox="0 0 760 434" preserveAspectRatio="none" aria-hidden="true">
      <path class="wave--wine" d="M0,200 C220,160 430,240 760,340 L760,434 L0,434 Z"/>
      <path class="wave--coral" d="M0,214 C225,174 435,254 760,356 L760,434 L0,434 Z"/>
      <path class="wave--ink" d="M0,228 C230,190 440,268 760,372 L760,434 L0,434 Z"/>
    </svg>
    <div class="wordmark">
      <span class="wordmark__dot"></span>
      <span class="wordmark__name">VELUMO</span>
    </div>
    <p class="tagline">Melbourne Street Art<br>Walking Tours</p>
  </section>

  <section class="card card--back" aria-label="Card back">
    <svg class="card__waves" viewBox="0 0 760 434" preserveAspectRatio="none" aria-hidden="true">
      <path class="wave--wine" d="M0,150 C210,110 420,200 760,320 L760,434 L0,434 Z"/>
      <path class="wave--coral" d="M0,164 C215,124 425,214 760,336 L760,434 L0,434 Z"/>
      <path class="wave--ink" d="M0,178 C220,140 430,228 760,352 L760,434 L0,434 Z"/>
    </svg>
    <div class="wordmark">
      <span class="wordmark__dot"></span>
      <span class="wordmark__name">VELUMO</span>
    </div>

    <ul class="contacts">
      <li>
        <svg viewBox="0 0 26 26" aria-hidden="true">
          <circle cx="13" cy="13" r="13" fill="var(--signal-red)"/>
          <path d="M9 7 L11.5 7 L12.5 10.5 L11 12 C11.8 14 12.6 14.8 14.5 15.5 L16 14 L19 15 L19 17.5 C19 18.5 18 19 17 19 C12 18.5 7.5 14 7 9 C7 8 8 7 9 7 Z" fill="var(--white)"/>
        </svg>
        <span>0481 556 217</span>
      </li>
      <li>
        <svg viewBox="0 0 26 26" aria-hidden="true">
          <circle cx="13" cy="13" r="13" fill="var(--signal-red)"/>
          <rect x="6.5" y="8.5" width="13" height="9" fill="var(--white)"/>
          <path d="M6.5 8.5 L13 14 L19.5 8.5" fill="none" stroke="var(--signal-red)" stroke-width="1.4"/>
        </svg>
        <span>bookings@velumo.com.au</span>
      </li>
      <li>
        <svg viewBox="0 0 26 26" aria-hidden="true">
          <circle cx="13" cy="13" r="13" fill="var(--signal-red)"/>
          <g fill="none" stroke="var(--white)" stroke-width="1.4">
            <circle cx="13" cy="13" r="7"/>
            <ellipse cx="13" cy="13" rx="3" ry="7"/>
            <line x1="6" y1="13" x2="20" y2="13"/>
            <line x1="7.5" y1="9.5" x2="18.5" y2="9.5"/>
            <line x1="7.5" y1="16.5" x2="18.5" y2="16.5"/>
          </g>
        </svg>
        <span>www.velumo.com.au</span>
      </li>
    </ul>

    <svg class="price-badge" viewBox="0 0 110 150" aria-label="Price $20">
      <path d="M40 60 L20 140 L38 128 L46 146 L58 68 Z" fill="var(--signal-red)"/>
      <path d="M62 60 L90 138 L72 130 L66 148 L50 68 Z" fill="#c81e1e"/>
      <circle cx="55" cy="50" r="40" fill="var(--signal-red)"/>
      <text class="price-badge__text" x="55" y="59" text-anchor="middle">$20</text>
    </svg>

    <ul class="details">
      <li>
        <svg viewBox="0 0 22 22" aria-hidden="true"><circle cx="11" cy="11" r="9.5" fill="none" stroke="var(--signal-red)" stroke-width="2.5"/><circle cx="11" cy="11" r="4" fill="var(--signal-red)"/></svg>
        <span>One Hour</span>
      </li>
      <li>
        <svg viewBox="0 0 22 22" aria-hidden="true"><circle cx="11" cy="11" r="9.5" fill="none" stroke="var(--signal-red)" stroke-width="2.5"/><circle cx="11" cy="11" r="4" fill="var(--signal-red)"/></svg>
        <span>Tours Daily</span>
      </li>
      <li>
        <svg viewBox="0 0 22 22" aria-hidden="true"><circle cx="11" cy="11" r="9.5" fill="none" stroke="var(--signal-red)" stroke-width="2.5"/><circle cx="11" cy="11" r="4" fill="var(--signal-red)"/></svg>
        <span>Meet at Carrow Rd Terminal</span>
      </li>
    </ul>
  </section>

</main>
</body>
</html>
```